Verpackungsdesign für Parfüm gesucht
Zielgruppe
Wir werden eine Marke unter dem Namen ORMAL mit Parfüm auf dem Markt bringen und benötigen hierfür ein hochwertiges Design . Unsre Zielgruppe ist m/w/d und zwischen 16 und 60 Jahre.
Aufgabenstellung
Bei der Verpackung handelt es sich um eine Schiebeschachtel. Wir benötigen das Design nur für die Außenhülle, nicht für den Schuber.
Pflichtangaben auf der Verpackung sind unser Logo, Eau de Parfum, High Intense, 20 ml e 0.67 FL OZ,
Natural Spray Vaporisateur,

```html
<!DOCTYPE html>
<html lang="en">
<head>
<meta charset="utf-8">
<title>ORMAL – Eau de Parfum sleeve</title>
<link rel="stylesheet" href="https://fonts.googleapis.com/css2?family=Montserrat:wght@300;400&display=swap">
<style>
  :root {
    --backdrop: #cfd0d2;
    --sleeve-black: #000000;
    --flap-black: #151515;
    --spine-black: #0b0b0b;
    --fold-line: #3a3a3a;
    --glue-line: #1f5a2a;
    --ink-light: #e6e6e6;
    --ink-soft: #cfcfcf;
    --facet-light: #1f1f1f;
  }
  html, body {
    margin: 0;
    padding: 0;
    width: 800px;
    height: 1200px;
    overflow: hidden;
    background: var(--backdrop);
  }
  .sleeve-net {
    display: block;
    width: 800px;
    height: 1200px;
  }
  .brand-name {
    font-family: "Montserrat", sans-serif;
    font-weight: 300;
    fill: var(--ink-light);
    letter-spacing: 0.12em;
  }
  .product-line {
    font-family: "Montserrat", sans-serif;
    font-weight: 400;
    fill: var(--ink-soft);
  }
</style>
</head>
<body>
<svg class="sleeve-net" viewBox="0 0 800 1200" xmlns="http://www.w3.org/2000/svg">
  <defs>
    <linearGradient id="facet-fade" x1="0" y1="0" x2="0" y2="1">
      <stop offset="0" stop-color="#000000"/>
      <stop offset="1" stop-color="#1f1f1f"/>
    </linearGradient>
  </defs>

  <g class="net" transform="translate(20 397)">
    <!-- glue flap -->
    <polygon class="glue-flap" points="0,22 88,0 88,405 0,405" fill="var(--flap-black)"/>
    <!-- left spine -->
    <rect class="spine spine-left" x="88" y="0" width="69" height="405" fill="var(--spine-black)"/>
    <!-- front panel -->
    <rect class="panel panel-front" x="157" y="0" width="267" height="405" fill="var(--sleeve-black)"/>
    <!-- right spine -->
    <rect class="spine spine-right" x="424" y="0" width="69" height="405" fill="var(--spine-black)"/>
    <!-- back panel -->
    <rect class="panel panel-back" x="493" y="0" width="266" height="405" fill="var(--sleeve-black)"/>

    <!-- faceted background texture areas -->
    <rect class="facet-area" x="157" y="194" width="267" height="211" fill="url(#facet-fade)" role="img" aria-label="Faint angular line pattern on dark background"/>
    <rect class="facet-area" x="493" y="194" width="266" height="211" fill="url(#facet-fade)" role="img" aria-label="Faint angular line pattern on dark background"/>

    <!-- fold lines -->
    <line x1="88" y1="0" x2="88" y2="405" stroke="var(--glue-line)" stroke-width="1"/>
    <line x1="157" y1="0" x2="157" y2="405" stroke="var(--fold-line)" stroke-width="1"/>
    <line x1="424" y1="0" x2="424" y2="405" stroke="var(--fold-line)" stroke-width="1"/>
    <line x1="493" y1="0" x2="493" y2="405" stroke="var(--fold-line)" stroke-width="1"/>

    <!-- front panel text -->
    <text class="brand-name" x="290" y="84" font-size="40" text-anchor="middle">ORMAL</text>
    <text class="product-line" x="290" y="125" font-size="14" text-anchor="middle">Eau de Parfum</text>
    <text class="product-line" x="290" y="144" font-size="14" text-anchor="middle">High Intense</text>
    <text class="product-line" x="290" y="377" font-size="14" text-anchor="middle">ml e 0.67 FL OZ 20</text>

    <!-- left spine text -->
    <g transform="translate(122.5 0) rotate(90)">
      <text class="product-line" x="153" y="5" font-size="13" text-anchor="middle">Natural Spray Vaporisateur</text>
      <text class="brand-name" x="327" y="9" font-size="24" text-anchor="middle">ORMAL</text>
    </g>

    <!-- right spine text -->
    <g transform="translate(458.5 0) rotate(90)">
      <text class="product-line" x="153" y="5" font-size="13" text-anchor="middle">Natural Spray Vaporisateur</text>
      <text class="brand-name" x="327" y="9" font-size="24" text-anchor="middle">ORMAL</text>
    </g>
  </g>
</svg>
</body>
</html>
```